The Little Meadow Biscuit Bakery Swing Tag Label Design/Logo

Hi! We are looking for a “swing tag” label design for our different flavoured packs of (6) cookies. Basic info on the front (business name “The Little Meadow Biscuit Bakery”, strap line being “Handmade Gourmet Cookies” (not made in Norfolk) and the flavour “Choc Chip”, “Original”, “Choc Orange”, etc…).
The flavour part of the label being colour coded to suit, so dark brown for choc chip, beige for original, orange for choc orange, red/white for cranberry & white choc, bla bla bla!!
The rear of the tag to display ingredients, barcode, business postcode, suitable for Vegans, Dairy Free, Truly Fenmoor Logo and Net Weight 300g.
Packaging is clear cellophane bags, with crimp seal. Three cookies stacked side by side with a brown Jute string tied around the packaging which will hold the tag.
We are selling in farm shops, deli’s and local food stores, so want to have a modern/smart feel to the design, yet retain the appeal of a small “cottage industry/countryside” style business.
The attached image is where we have got so far (with our very basic design skills) , but do not let this guide you too much, as we are looking for inspiration. (Appreciate the attached does not have the cottage/country appeal)!!
Size is undetermined, but thinking 100mm x 50mm, ish? Not ruled out a round label either, being cookies?
Labels will also be the basis for our business cards, internet pages (facebook, Instagram, etc…), so the design wants to be catchy, instantly recognisable and “say what it does on the tin”.
We also have single pack cookies in cellophane bags, so would be great if the deign could be printed in sticky label format also.
Not decided if the labels will be “craft paper” brown tags, or white, or another colour. Open to suggestions.
Like the idea of the “bite” out of the cookie, but needs “some teeth” if you get what I mean.
Feel free to message if you wish!
Thanks for your time.

The Little Meadow Biscuit Bakery or THE LITTLE MEADOW BISCUIT BAKERY

```html
<!DOCTYPE html>
<html lang="en">
<head>
<meta charset="utf-8">
<title>The Little Meadow Biscuit Bakery – Swing Tag</title>
<link rel="stylesheet" href="https://fonts.googleapis.com/css2?family=Jost:wght@400;600&display=swap">
<style>
  :root {
    --tag-charcoal: #2b2928;
    --cookie-brown: #9c5322;
    --ink-dark: #2b2928;
    --paper-white: #ffffff;
  }
  html, body {
    margin: 0;
    padding: 0;
    width: 1200px;
    height: 2396px;
    overflow: hidden;
    background: var(--tag-charcoal);
  }
  .swing-tag {
    position: relative;
    width: 1200px;
    height: 2396px;
    background: var(--tag-charcoal);
    font-family: "Jost", "Futura", sans-serif;
    overflow: hidden;
  }
  .string-hole {
    position: absolute;
    left: 125px;
    top: 125px;
    width: 102px;
    height: 102px;
    border-radius: 50%;
    background: var(--paper-white);
  }
  .brand-name {
    position: absolute;
    right: 66px;
    top: 390px;
    margin: 0;
    text-align: right;
    color: var(--paper-white);
    font-weight: 600;
    line-height: 1;
  }
  .brand-name .brand-line {
    display: block;
  }
  .brand-name .brand-line--lead {
    font-size: 96px;
    margin-bottom: 34px;
  }
  .brand-name .brand-line--main {
    font-size: 168px;
    letter-spacing: 4px;
    text-transform: uppercase;
  }
  .flavour-badge {
    position: absolute;
    left: 72px;
    top: 898px;
    width: 304px;
    height: 304px;
    border-radius: 50%;
    background: var(--cookie-brown);
    display: flex;
    align-items: center;
    justify-content: center;
    text-align: center;
    color: var(--ink-dark);
    font-size: 74px;
    font-weight: 400;
    line-height: 0.95;
  }
  .strapline {
    position: absolute;
    left: 1028px;
    bottom: 72px;
    margin: 0;
    writing-mode: vertical-rl;
    transform: rotate(180deg);
    color: var(--cookie-brown);
    font-size: 90px;
    font-weight: 400;
    letter-spacing: 1px;
    line-height: 1;
    white-space: nowrap;
  }
</style>
</head>
<body>
  <main class="swing-tag">
    <div class="string-hole" aria-hidden="true"></div>

    <h1 class="brand-name">
      <span class="brand-line brand-line--lead">The Little Meadow</span>
      <span class="brand-line brand-line--main">Biscuit</span>
      <span class="brand-line brand-line--main">Bakery</span>
    </h1>

    <div class="flavour-badge">
      <span>choco<br>chip</span>
    </div>

    <p class="strapline">Handmade Gourmet Cookies</p>
  </main>
</body>
</html>
```